Sunny Paths and joy Business card

I have a logo, but will like a business card design. Is for a travel agency in Mexico. We focus in family experiences.

I will liek some thing different and unique, from the traditional business card, something to get remmeber for.

Business card information:

Leandro T. Ocampo
leandro@sunnypathsjoy.example

Alameda 482, 3 piso
Col. Tlalpizco
Mexico, D.F. 07320

office: (55) 5000-0142
mobile: (55) 9000-0187

www.sunnypathsjoy.example
@sunnypjoy
blog: sunnypathsandjoy.blogsite.example
social: SunnyPathsAndJoy

```html
<!DOCTYPE html>
<html lang="en">
<head>
<meta charset="utf-8">
<title>Sunny Paths and joy – Business Card</title>
<link rel="stylesheet" href="https://fonts.googleapis.com/css2?family=Noticia+Text&family=PT+Serif&display=swap">
<style>
  :root {
    --panel-blue: #175a8a;
    --card-white: #ffffff;
    --ink-blue: #1d5f92;
    --ink-dark: #222222;
    --sky-light: #cfe6f5;
    --sky-mid: #8fc3e6;
    --label-ink: #222222;
  }
  * { margin: 0; padding: 0; box-sizing: border-box; }
  html, body {
    width: 1200px; height: 684px; overflow: hidden; background: #ffffff;
  }
  .sheet { position: relative; width: 1200px; height: 684px; }
  .panel {
    position: absolute; top: 8px; width: 590px; height: 590px;
    background: var(--panel-blue); border-radius: 30px; overflow: hidden;
  }
  .panel--front { left: 0; }
  .panel--back { left: 610px; }
  .card {
    position: absolute; left: 52px; top: 52px; width: 490px; height: 490px;
    background: var(--card-white); border-radius: 22px;
    font-family: "Noticia Text", serif; text-align: center;
  }
  .card--front { transform: rotate(-13deg); }
  .card--back { transform: rotate(15deg); }
  .card__art {
    position: absolute; left: 95px; top: 22px; width: 300px; height: 190px;
    border-radius: 95px;
    background: radial-gradient(ellipse at 55% 45%, var(--sky-mid), var(--sky-light) 70%, #eaf4fb);
  }
  .card__brand {
    position: absolute; left: 0; right: 0; top: 220px;
    font-size: 44px; line-height: 56px; color: var(--ink-blue); white-space: nowrap;
  }
  .card__contact { position: absolute; left: 0; right: 0; top: 318px; }
  .card__name { font-size: 34px; color: var(--ink-dark); line-height: 42px; }
  .card__line { font-size: 26px; color: var(--ink-blue); line-height: 32px; white-space: nowrap; }
  .card__details { position: absolute; left: 0; right: 0; top: 92px; }
  .card__details .card__line { font-size: 27px; line-height: 32px; }
  .card__gap { height: 22px; }
  .card__details .card__line--long { font-size: 25px; }
  .label {
    position: absolute; top: 624px; width: 300px;
    font-family: "PT Serif", serif; font-size: 56px; color: var(--label-ink);
    text-align: center;
  }
  .label--front { left: 125px; }
  .label--back { left: 755px; }
</style>
</head>
<body>
<main class="sheet">
  <section class="panel panel--front">
    <div class="card card--front">
      <div class="card__art" role="img" aria-label="Illustration of a family flying in a cheerful blue airplane over a pale sky"></div>
      <div class="card__brand">Sunny Paths and joy</div>
      <div class="card__contact">
        <p class="card__name">Leandro T. Ocampo</p>
        <p class="card__line">leandro@sunnypathsjoy.example</p>
        <p class="card__line">office: (55) 5000-0142</p>
        <p class="card__line">mobile: (55) 9000-0187</p>
      </div>
    </div>
  </section>

  <section class="panel panel--back">
    <div class="card card--back">
      <div class="card__details">
        <p class="card__line">ADDRESS:</p>
        <p class="card__line">Alameda 482, 3 piso</p>
        <p class="card__line">Col. Tlalpizco</p>
        <p class="card__line">Mexico, D.F. 07320</p>
        <div class="card__gap"></div>
        <p class="card__line">www.sunnypathsjoy.example</p>
        <p class="card__line">@sunnypjoy</p>
        <p class="card__line">blog:</p>
        <p class="card__line card__line--long">sunnypathsandjoy.blogsite.example</p>
        <p class="card__line">social:</p>
        <p class="card__line">SunnyPathsAndJoy</p>
      </div>
    </div>
  </section>

  <p class="label label--front">Front</p>
  <p class="label label--back">Back</p>
</main>
</body>
</html>
```